Vela group business advertisement

i am happy to extend deadline and pay for 2nd price
Looking for a simple brochure about my company. I HAVE ATTACHED 2 PICTURES OF WHAT THE BROCHURE SIZE SHOULD BE (A4) fold out
We would like to hand it out to clients and get their attention of the services we provide. Which are,
telephone number
0491 276 305
unit 3/9 Harlow Pl Crestwood N.S.W 2620
EMAIL: info@velagroup-example.com.au
web: www.velagroup-example.com.au

Car park sweeping and scrubbing
High pressure cleaning
Builders clean
Strip and sealing floors

also must include a section so i can put information about each topic next to the picture
also have on last page ABOUT VELA GROUP
there are 2 designers that i have gave stars who are on the right path

Target Market(s)

Body corporate
Builders
Shopping Centres
office carparks

Industry/Entity Type

Cleaning Service

Coding

Coded - Design and coding required

Font styles to use
Other font styles liked:
• futura

Colors
3377b5
86cae7
34a6d7
cadf82
fdf9cf
cfcfcf
b1b1b1

Requirements
Must have
• Pictures in relation to the services we provide and equipment used.
• Dot point
• #S30 brolan sweeper
• #5700 brolan scubbers
• #portable high pressure cleaning
• we attached pictures of machines
Nice to have
• Vela Group logo
• Bold eye catching colors for the service. eg,blue and grey,
• Light background color for the whole brochure.
Should not have
• please not tri fold

```html
<!DOCTYPE html>
<html lang="en">
<head>
<meta charset="utf-8">
<title>Vela Group – Service Brochure</title>
<link rel="stylesheet" href="https://fonts.googleapis.com/css2?family=Roboto:wght@300;400;700&display=swap">
<style>
  :root {
    --bg: #ededed;
    --paper: #ffffff;
    --teal: #2497a6;
    --blue: #2b7ba3;
    --sky: #34a6d7;
    --grey-dark: #6b6b6b;
    --grey-mid: #b1b1b1;
    --grey-light: #e4e4e4;
    --ink: #2e2e2e;
    --ink-soft: #6a6a6a;
  }
  * { box-sizing: border-box; margin: 0; padding: 0; }
  html, body { width: 1041px; height: 1200px; overflow: hidden; }
  body {
    background: var(--bg);
    font-family: "Roboto", Arial, sans-serif;
    color: var(--ink);
    position: relative;
  }
  .spread {
    position: absolute;
    left: 110px;
    width: 820px;
    height: 580px;
    display: flex;
    box-shadow: 0 8px 24px rgba(0,0,0,.18);
  }
  .spread--cover { top: 14px; }
  .spread--inside { top: 606px; }
  .page {
    position: relative;
    width: 410px;
    height: 580px;
    background: var(--paper);
    overflow: hidden;
  }
  .page + .page { border-left: 1px solid #dcdcdc; }
  .block { position: absolute; }
  .photo { position: absolute; }
  .brand {
    position: absolute;
    display: flex;
    align-items: center;
    gap: 8px;
    font-weight: 700;
    color: var(--blue);
    letter-spacing: 2px;
    white-space: nowrap;
  }
  .brand__mark { background: var(--sky); display: block; }

  /* cover – back */
  .contact {
    position: absolute;
    left: 56px; top: 440px;
    font-size: 13px;
    line-height: 18px;
    color: var(--ink-soft);
  }
  /* cover – front */
  .service-list {
    position: absolute;
    left: 254px; top: 360px;
    list-style: none;
    font-size: 8.5px;
    line-height: 12px;
    color: #fff;
    text-transform: uppercase;
    letter-spacing: .3px;
  }

  /* inside */
  .heading {
    position: absolute;
    font-size: 19px;
    font-weight: 300;
    letter-spacing: .5px;
    color: var(--ink);
    text-transform: uppercase;
    line-height: 1.15;
    white-space: nowrap;
  }
  .heading strong { font-weight: 700; }
  .body-copy {
    position: absolute;
    font-size: 8.5px;
    line-height: 11px;
    color: var(--ink);
  }
  .quote {
    position: absolute;
    left: 28px; top: 222px;
    width: 356px; height: 40px;
    border: 1.5px dashed var(--sky);
    display: flex;
    align-items: center;
    justify-content: center;
    gap: 8px;
    font-size: 18px;
    letter-spacing: 1px;
    white-space: nowrap;
  }
  .quote__lead { color: var(--grey-mid); font-weight: 300; }
  .quote__call { color: var(--sky); font-weight: 700; }
</style>
</head>
<body>

<!-- Outside cover -->
<section class="spread spread--cover">
  <div class="page page--back">
    <div class="block" style="left:264px;top:310px;width:146px;height:180px;background:var(--grey-dark)"></div>
    <div class="block" style="left:14px;top:380px;width:26px;height:160px;background:var(--teal)"></div>
    <div class="brand" style="left:56px;top:396px;font-size:17px">
      <span class="brand__mark" style="width:14px;height:14px"></span>VELA GROUP
    </div>
    <p class="contact">
      Phone: 300 555 019<br>
      info@velagroup-example.com.au<br>
      www.velagroup-example.com.au
    </p>
  </div>

  <div class="page page--front">
    <div class="brand" style="left:112px;top:150px;font-size:24px">
      <span class="brand__mark" style="width:20px;height:20px"></span>VELA GROUP
    </div>
    <div class="block" style="left:0;top:300px;width:410px;height:170px;background:var(--grey-light)"></div>
    <div class="photo" role="img" aria-label="Polished shopping centre floor with bright reflections"
         style="left:14px;top:300px;width:220px;height:140px;background:linear-gradient(180deg,#4a4f55 0%,#9ea3a6 45%,#e7e8e8 100%)"></div>
    <div class="block" style="left:242px;top:284px;width:168px;height:156px;background:var(--blue)"></div>
    <ul class="service-list">
      <li>Car park sweeping and scrubbing</li>
      <li>High pressure cleaning</li>
      <li>Builders clean</li>
      <li>Strip and sealing floors</li>
    </ul>
  </div>
</section>

<!-- Inside spread -->
<section class="spread spread--inside">
  <div class="page page--left">
    <div class="brand" style="left:20px;top:24px;font-size:12px">
      <span class="brand__mark" style="width:10px;height:10px"></span>VELA GROUP
    </div>
    <h2 class="heading" style="left:128px;top:28px">High pressure <strong>cleaning</strong></h2>
    <div class="block" style="left:0;top:66px;width:410px;height:122px;background:var(--grey-light)"></div>
    <div class="photo" role="img" aria-label="Worker using a high pressure cleaner on pavement"
         style="left:0;top:72px;width:250px;height:108px;background:linear-gradient(135deg,#c9c6bd 0%,#8e8c86 60%,#d8d4c6 100%)"></div>
    <div class="block" style="left:262px;top:72px;width:148px;height:108px;background:var(--grey-mid)"></div>
    <p class="body-copy" style="left:60px;top:200px;width:250px">
      Our portable high pressure units lift oil, gum, grime and tyre marks from concrete, pavers and walls. We work around your trading hours, recycle water where possible and leave every surface safe, bright and ready for foot traffic.
    </p>
    <h2 class="heading" style="left:60px;top:290px">Strip and sealing <strong>floors</strong></h2>
    <div class="block" style="left:0;top:322px;width:410px;height:150px;background:var(--grey-light)"></div>
    <div class="block" style="left:14px;top:350px;width:48px;height:196px;background:var(--blue)"></div>
    <div class="photo" role="img" aria-label="Freshly sealed glossy floor with a ride-on floor scrubber"
         style="left:70px;top:330px;width:300px;height:230px;background:linear-gradient(180deg,#d6dde0 0%,#eef1f2 45%,#2f6b70 70%,#1f4e54 100%)"></div>
  </div>

  <div class="page page--right">
    <h2 class="heading" style="left:28px;top:26px"><strong>Builders</strong> clean</h2>
    <div class="block" style="left:0;top:60px;width:410px;height:122px;background:var(--grey-light)"></div>
    <div class="photo" role="img" aria-label="Empty new building interior with a clean concrete floor"
         style="left:28px;top:66px;width:124px;height:108px;background:linear-gradient(180deg,#b7b9b3 0%,#e3e3de 50%,#7f8a88 100%)"></div>
    <div class="block" style="left:152px;top:56px;width:60px;height:118px;background:var(--teal)"></div>
    <p class="body-copy" style="left:222px;top:30px;width:172px">
      After the trades leave, our crew removes dust, paint spots, plaster and debris from every room. Windows, fittings and floors are detailed so the site is ready for handover and the new owners on day one.
    </p>
    <div class="quote">
      <span class="quote__lead">GET A QUOTE!</span>
      <span class="quote__call">CALL 300 555 019</span>
    </div>
    <h2 class="heading" style="left:28px;top:286px">Car park<br><strong>sweeping and scrubing</strong></h2>
    <div class="block" style="left:0;top:342px;width:410px;height:150px;background:var(--grey-light)"></div>
    <div class="block" style="left:300px;top:300px;width:110px;height:156px;background:var(--teal)"></div>
    <div class="photo" role="img" aria-label="Ride-on sweeper in an empty underground car park"
         style="left:40px;top:342px;width:270px;height:200px;background:linear-gradient(180deg,#c4c8c9 0%,#8d9596 50%,#2aa3a5 78%,#5b6466 100%)"></div>
  </div>
</section>

</body>
</html>
```